Square graphic for social media post

I want to create a 1080 x 1080px all-black image for the quote below that I can share on social media. I want the emphasis to be primarily on the quote, secondarily on the portrait, and third (smallest) on the logo. I want the background on the portrait to be edited so it's transparent and just shows the face of the person on a black background (no brick wall visible).

Graphic color: black
Text color: white
Content: "What we went through is going to make the greatest generation of hoteliers our industry has ever seen." << biggest text
Dorian Welk << smaller text
President, Marrowgate Hotels << smaller text
[image of person - use whichever version looks better to you]
[Add Lodging Ledger logo - whichever looks better to you]

This image needs to be readable when sized down much smaller (400x400?) so want the text and portrait to take up most of the space.

I'd like the output both as PNG and original file (preferably Canva). Thanks!

Target Market(s)

Hotel managers

Industry/Entity Type

Hospitality

Font styles to use
Sans Serif

Colors

Designer to choose colors to be used in the design.

Requirements
Must have
• Needs to focus on the quote and the person quoted (the portrait)

```html
<!DOCTYPE html>
<html lang="en">
<head>
<meta charset="utf-8">
<title>Dorian Welk Quote Card</title>
<link rel="stylesheet" href="https://fonts.googleapis.com/css2?family=Roboto:ital,wght@0,400;0,500;1,300;1,400;1,800&family=Roboto+Slab:wght@500&display=swap">
<style>
  :root {
    --bg: #111214;
    --bg-glow: #222222;
    --ink: #ffffff;
    --ink-soft: #f2f2f2;
    --portrait-edge: #2a2a2b;
    --portrait-core: #6a5a52;
  }
  * { margin: 0; padding: 0; box-sizing: border-box; }
  html, body {
    width: 1200px;
    height: 1200px;
    overflow: hidden;
    background: var(--bg);
  }
  .quote-card {
    position: relative;
    width: 1200px;
    height: 1200px;
    background:
      radial-gradient(ellipse 520px 360px at 600px 1120px, var(--bg-glow) 0%, rgba(34,34,34,0) 100%),
      var(--bg);
    color: var(--ink);
    font-family: "Roboto", sans-serif;
  }
  .brand {
    position: absolute;
    top: 138px;
    left: 0;
    width: 100%;
    display: flex;
    justify-content: center;
    align-items: center;
    gap: 10px;
  }
  .brand-dot {
    width: 8px;
    height: 8px;
    border-radius: 50%;
    background: var(--ink);
  }
  .brand-name {
    font-family: "Roboto", sans-serif;
    font-weight: 500;
    font-size: 15px;
    letter-spacing: 5px;
    text-transform: uppercase;
    color: var(--ink);
  }
  .quote {
    position: absolute;
    top: 262px;
    left: 0;
    width: 100%;
    text-align: center;
    font-weight: 800;
    font-style: italic;
    font-size: 69px;
    line-height: 87px;
    letter-spacing: -0.5px;
  }
  .quote-line { display: block; white-space: nowrap; }
  .quote-line--first { padding-left: 40px; }
  .quote-mark {
    position: absolute;
    font-family: "Roboto Slab", serif;
    font-weight: 500;
    font-size: 64px;
    line-height: 1;
    color: var(--ink);
  }
  .quote-mark--open { left: 147px; top: 238px; }
  .quote-mark--close { left: 1000px; top: 560px; }
  .attribution {
    position: absolute;
    top: 643px;
    left: 0;
    width: 100%;
    display: flex;
    justify-content: center;
    align-items: baseline;
    gap: 14px;
    color: var(--ink-soft);
    font-style: italic;
  }
  .attribution-name {
    font-weight: 400;
    font-size: 49px;
  }
  .attribution-role {
    font-weight: 400;
    font-size: 27px;
  }
  .portrait {
    position: absolute;
    left: 412px;
    top: 763px;
    width: 376px;
    height: 376px;
    border-radius: 50%;
    background: radial-gradient(circle at 50% 52%, var(--portrait-core) 0%, #4a3f3a 38%, var(--portrait-edge) 72%);
  }
</style>
</head>
<body>
  <main class="quote-card">
    <div class="brand">
      <span class="brand-dot"></span>
      <span class="brand-name">Lodging Ledger</span>
    </div>

    <span class="quote-mark quote-mark--open" aria-hidden="true">&ldquo;</span>
    <blockquote class="quote">
      <span class="quote-line quote-line--first">What we went through is</span>
      <span class="quote-line">going to make the greatest</span>
      <span class="quote-line">generation of hoteliers our</span>
      <span class="quote-line">industry has ever seen.</span>
    </blockquote>
    <span class="quote-mark quote-mark--close" aria-hidden="true">&rdquo;</span>

    <p class="attribution">
      <span class="attribution-name">Dorian Welk</span>
      <span class="attribution-role">President, Marrowgate Hotels</span>
    </p>

    <div class="portrait" role="img" aria-label="Circular portrait photo of Dorian Welk, smiling, in a navy blazer and white shirt on a dark background"></div>
  </main>
</body>
</html>
```